Business Card Design

We are a commercial real estate brokerage in San Francisco, leasing office buildings downtown.
I would like a clean, elegant look. Simple but powerful .

Industry/Entity Type

Business

Contact Information for Business Card

Derek Hollings
lic# 02875140
415.287.6041
derek@vexa-commercial.com
vexa-commercial.com

```html
<!DOCTYPE html>
<html lang="en">
<head>
<meta charset="utf-8">
<title>Vexa Commercial – Business Card</title>
<link rel="stylesheet" href="https://fonts.googleapis.com/css2?family=Open+Sans:wght@400;600&display=swap">
<style>
  :root {
    --backdrop: #ebe5d7;
    --card-front: #ffffff;
    --card-back: #dcdcdc;
    --slate: #7886a4;
    --slate-light: #b7bdcb;
    --ink-light: #ffffff;
    --brand: #6f7b99;
  }
  * { margin: 0; padding: 0; box-sizing: border-box; }
  html, body {
    width: 1200px;
    height: 510px;
    overflow: hidden;
    background: var(--backdrop);
    font-family: "Open Sans", Arial, sans-serif;
  }
  .canvas {
    position: relative;
    width: 1200px;
    height: 510px;
  }
  .card {
    position: absolute;
    top: 132px;
    width: 418px;
    height: 246px;
    border-radius: 14px;
    box-shadow: 0 6px 14px rgba(0,0,0,0.18);
  }
  .card--front {
    left: 157px;
    background: var(--card-front);
    display: flex;
    align-items: center;
    justify-content: center;
  }
  .card--back {
    left: 624px;
    background: var(--card-back);
  }
  .brand {
    display: flex;
    align-items: center;
    gap: 14px;
  }
  .brand__square {
    width: 28px;
    height: 28px;
    background: var(--brand);
  }
  .brand__name {
    font-weight: 600;
    font-size: 30px;
    letter-spacing: 1px;
    color: var(--brand);
    line-height: 1;
  }
  .bar {
    position: absolute;
    left: 184px;
    background: var(--slate);
    color: var(--ink-light);
    font-size: 9.5px;
    line-height: 15px;
    padding-left: 18px;
    white-space: nowrap;
  }
  .bar--name {
    top: 61px;
    width: 234px;
    height: 16px;
    padding-left: 6px;
    font-size: 11px;
    line-height: 16px;
  }
  .accent-band {
    position: absolute;
    left: 184px;
    top: 81px;
    width: 234px;
    height: 17px;
    background: var(--slate-light);
  }
  .bar--license { top: 105px; width: 156px; height: 15px; }
  .bar--phone   { top: 126px; width: 156px; height: 15px; }
  .bar--email   { top: 147px; width: 234px; height: 16px; line-height: 16px; }
  .bar--web     { top: 169px; width: 234px; height: 16px; line-height: 16px; }
</style>
</head>
<body>
<main class="canvas">
  <section class="card card--front" aria-label="Card front">
    <div class="brand">
      <span class="brand__square" aria-hidden="true"></span>
      <span class="brand__name">VEXA COMMERCIAL</span>
    </div>
  </section>

  <section class="card card--back" aria-label="Card back">
    <div class="bar bar--name">Derek Hollings</div>
    <div class="accent-band" role="img" aria-label="Diagonal striped accent band"></div>
    <div class="bar bar--license">lic# 02875140</div>
    <div class="bar bar--phone">415.287.6041</div>
    <div class="bar bar--email">derek@vexa-commercial.com</div>
    <div class="bar bar--web">vexa-commercial.com</div>
  </section>
</main>
</body>
</html>
```